Web design for a Crane & Heavy Equipment Inspection, Repair and Maintenance Company in Texas

We need a web design for a new company based in Houston, Texas called "Bristen Hoist & Equipment". We inspect, repair and maintain diesel driven heavy equipment, generators, fire water pumps and cranes. We would like to see designs that use the colors orange, white, yellow and brown, and/or orange, white, navy, yellow and grey.

```html
<!DOCTYPE html>
<html lang="en">
<head>
<meta charset="utf-8">
<title>Bristen Hoist &amp; Equipment</title>
<link href="https://fonts.googleapis.com/css2?family=Ubuntu:wght@300;400;500;700&display=swap" rel="stylesheet">
<style>
:root{
  --orange:#f26c3a;
  --navy:#0f3f6b;
  --navy-deep:#0c2b4a;
  --navy-dark:#08213a;
  --yellow:#f5d60e;
  --white:#ffffff;
  --ink:#0f3f6b;
  --sky:#4a8fd0;
}
*{box-sizing:border-box;margin:0;padding:0}
html,body{width:686px;height:1200px;overflow:hidden}
body{font-family:"Ubuntu",sans-serif;color:var(--white);background:var(--navy);position:relative}
.topbar{position:absolute;left:0;top:0;width:686px;height:16px;background:var(--orange);font-size:5.5px;text-align:right;padding:5px 108px 0 0}
.topbar strong{font-weight:700}
.nav{position:absolute;top:16px;left:0;width:686px;height:43px;background:var(--navy)}
.brand{position:absolute;left:108px;top:14px;font-weight:700;font-size:11px;letter-spacing:.3px;color:var(--white);display:flex;align-items:center;gap:5px}
.brand-dot{width:8px;height:8px;background:var(--orange);border-radius:50%}
.menu{position:absolute;right:109px;top:16px;display:flex;font-size:8px;gap:0}
.menu span{padding:0 9px;border-left:1px solid var(--white);line-height:8px}
.menu span:first-child{border-left:none}
.hero{position:absolute;top:59px;left:0;width:686px;height:286px;background:linear-gradient(120deg,#5f9fd8 0%,#8dbbe4 35%,#c93a2a 62%,#e0472f 80%,#7a3a2a 100%)}
.hero-title{position:absolute;right:122px;top:134px;font-size:15px;font-weight:300}
.arrow{position:absolute;top:121px;width:39px;height:45px;background:rgba(255,255,255,.22)}
.arrow.prev{left:68px}.arrow.next{right:68px}
.arrow svg{width:100%;height:100%}
.welcome{position:absolute;top:345px;left:0;width:686px;height:239px;background:var(--navy);text-align:center}
.section-title{font-size:13px;font-weight:400}
.welcome .section-title{margin-top:21px}
.welcome p{width:470px;margin:10px auto 0;font-size:5.6px;line-height:10.5px}
.services-title{margin-top:33px}
.services{display:flex;justify-content:space-between;width:347px;margin:16px auto 0}
.service{width:70px;text-align:center;font-size:9px}
.service svg{width:38px;height:38px;display:block;margin:0 auto 10px}
.team{position:absolute;top:584px;left:0;width:686px;height:244px;background:var(--orange);text-align:center}
.team .section-title{font-size:11px;margin-top:24px}
.leaders{display:flex;justify-content:space-between;width:464px;margin:16px auto 0}
.leader{width:140px}
.portrait{width:115px;height:98px;margin:0 auto;background:linear-gradient(180deg,#ffffff 0%,#f3e1d8 45%,#f59a72 100%);border-radius:8px 8px 50% 50%}
.leader h3{color:var(--ink);font-size:7.5px;font-weight:700;margin-top:8px}
.leader .role{color:var(--ink);font-size:5.5px;margin-top:1px}
.leader p{font-size:5.6px;line-height:11.5px;margin-top:12px}
.diffs{position:absolute;top:828px;left:0;width:686px;height:297px;background:linear-gradient(180deg,#0f3559 0%,#0c2b4a 60%,#0a2540 100%)}
.diffs .section-title{text-align:center;margin-top:21px}
.diff{position:absolute;display:flex;gap:8px;font-size:5.6px;line-height:8.7px;width:130px}
.num{flex:none;width:27px;height:27px;border-radius:50%;background:var(--white);color:var(--navy-deep);font-weight:700;font-size:15px;display:flex;align-items:center;justify-content:center}
.diff p{margin-top:-1px}
.rig{position:absolute;left:5px;top:200px;width:130px;height:97px;background:linear-gradient(180deg,rgba(242,108,58,0) 0%,rgba(242,108,58,.9) 55%,var(--orange) 100%);clip-path:polygon(40% 0,60% 0,62% 40%,100% 55%,100% 100%,0 100%,0 60%,38% 40%)}
.closing{position:absolute;left:0;top:248px;width:686px;text-align:center;font-size:5.8px;line-height:12px}
.footer{position:absolute;top:1125px;left:0;width:686px;height:75px;background:var(--orange);text-align:center}
.social{display:flex;justify-content:center;gap:6px;margin-top:13px}
.social span{width:15px;height:15px;border-radius:50%;background:var(--white)}
.footer-menu{display:flex;justify-content:center;font-size:8px;margin-top:7px}
.footer-menu span{padding:0 13px;border-left:1px solid var(--white);line-height:8px}
.footer-menu span:first-child{border-left:none}
.copyright{font-size:7.5px;margin-top:9px}
</style>
</head>
<body>
<div class="topbar">For Service &amp; Inspections <strong>Call: 832.555.0148</strong></div>

<header class="nav">
  <div class="brand"><span class="brand-dot"></span>BRISTEN HOIST &amp; EQUIPMENT</div>
  <nav class="menu"><span>Home</span><span>About Us</span><span>Services</span><span>Contact Us</span></nav>
</header>

<section class="hero" role="img" aria-label="Photo of a crane worker in a red coverall and yellow hard hat beside a red crane lifting pipes against a blue sky">
  <div class="arrow prev"><svg viewBox="0 0 39 45"><polyline points="24,10 12,22.5 24,35" fill="none" stroke="#fff" stroke-width="1.2"/></svg></div>
  <div class="hero-title">Bristen Hoist &amp; Equipment</div>
  <div class="arrow next"><svg viewBox="0 0 39 45"><polyline points="15,10 27,22.5 15,35" fill="none" stroke="#fff" stroke-width="1.2"/></svg></div>
</section>

<section class="welcome">
  <h1 class="section-title">Welcome To Bristen Hoist &amp; Equiment</h1>
  <p>Bristen Hoist and Equipment Services Company, LLC provides on-site crane, generator and heavy equipment repair, maintenance and inspection.&nbsp; Our commitment to our clients extends beyond our core values of safety, honesty, quality and reliability.&nbsp; We are leveraging technology to improve our clients’ access to inspection, maintenance and repair records.</p>
  <h2 class="section-title services-title">What We Do?</h2>
  <div class="services">
    <div class="service">
      <svg viewBox="0 0 38 38"><circle cx="15" cy="15" r="10" fill="none" stroke="var(--yellow)" stroke-width="4.5"/><line x1="22" y1="22" x2="33" y2="33" stroke="var(--yellow)" stroke-width="6" stroke-linecap="round"/></svg>
      Inspect
    </div>
    <div class="service">
      <svg viewBox="0 0 38 38"><rect x="3" y="14" width="32" height="20" rx="2" fill="var(--yellow)"/><rect x="12" y="9" width="14" height="6" rx="1" fill="none" stroke="var(--yellow)" stroke-width="2.5"/><line x1="6" y1="21" x2="32" y2="21" stroke="var(--navy)" stroke-width="1.5"/><line x1="8" y1="3" x2="14" y2="14" stroke="var(--yellow)" stroke-width="2.5"/><line x1="30" y1="3" x2="24" y2="14" stroke="var(--yellow)" stroke-width="2.5"/></svg>
      Repair
    </div>
    <div class="service">
      <svg viewBox="0 0 38 38"><path d="M9 15 A10 10 0 0 1 29 15 Z" fill="var(--yellow)"/><rect x="6" y="14" width="26" height="3" rx="1" fill="var(--yellow)"/><path d="M6 37 L9 27 Q19 22 29 27 L32 37 Z" fill="var(--yellow)"/></svg>
      Maintain
    </div>
  </div>
</section>

<section class="team">
  <h2 class="section-title">Our Team Leaders</h2>
  <div class="leaders">
    <div class="leader">
      <div class="portrait" role="img" aria-label="Portrait photo of the company president in a circle framed by a white pump jack silhouette"></div>
      <h3>Dana Whitfield</h3>
      <div class="role">President</div>
      <p>A Fortune 200 corporate sales leader, with 20 years’ experience in sales and management of multi-million dollar corporate accounts.</p>
    </div>
    <div class="leader">
      <div class="portrait" role="img" aria-label="Portrait photo of the general manager in a circle framed by a white pump jack silhouette"></div>
      <h3>Carl Whitfield</h3>
      <div class="role">General Manager</div>
      <p>A disabled veteran and former Department of Defense Electronic Commerce expert with 20 years’ experience in Information Technology.</p>
    </div>
    <div class="leader">
      <div class="portrait" role="img" aria-label="Portrait photo of the field service manager in a circle framed by a white pump jack silhouette"></div>
      <h3>Marcus Delaney</h3>
      <div class="role">Field Service Manager</div>
      <p>A 15 year Houston area expert in the crane and heavy equipment service industry.</p>
    </div>
  </div>
</section>

<section class="diffs" role="img" aria-label="Background photo of crane and construction silhouettes in dark blue">
  <h2 class="section-title">Our key Differentiators&nbsp; Are&nbsp; ?</h2>
  <div class="diff" style="left:113px;top:76px"><span class="num">1</span><p>Safety – Job Safety Analysis is completed on site, on-line - every time, with an integrated client approval process.</p></div>
  <div class="diff" style="left:256px;top:76px"><span class="num">2</span><p>Technicians electronically update service records from the field, for real-time status updates</p></div>
  <div class="diff" style="left:412px;top:76px"><span class="num">3</span><p>Contracted clients enjoy on-line access to job status and account history.</p></div>
  <div class="diff" style="left:113px;top:161px"><span class="num">4</span><p>Client driven communication options - you select who to keep in the loop with electronic job status updates.</p></div>
  <div class="diff" style="left:256px;top:161px"><span class="num">5</span><p>Streamlined, paper-free process for estimates and invoices, designed to meet your needs, with your equipment and purchase order numbers for prompt and efficient financial management.</p></div>
  <div class="diff" style="left:412px;top:161px"><span class="num">6</span><p>We are a woman owned small business, in the process of seeking WOBC certification.</p></div>
  <div class="rig" role="img" aria-label="Orange silhouette of an offshore oil rig"></div>
  <p class="closing">We would appreciate the opportunity to meet with you to demonstrate the industry leading service and efficiency that you would enjoy, as a client of<br>Bristen Hoist and Equipment Services Company, LLC.&nbsp; Thank you, in advance, for your consideration.</p>
</section>

<footer class="footer">
  <div class="social"><span></span><span></span><span></span></div>
  <nav class="footer-menu"><span>Home</span><span>About Us</span><span>Services</span><span>Contact Us</span></nav>
  <div class="copyright">Copyright © 2014 Bristen Hoist &amp; Equipment Services Company, LLC</div>
</footer>
</body>
</html>
```